Harbor Ridge Elementary School Letterhead

We would like a letterhead that includes our school mascot (Flicker the Falcon), school address, and phone number. We want something with personality and a little fun. Our school colors are navy blue, green (like the flag in our graphic), and gray. We included an example of a letterhead we like the feel of (on the fun side). The example is the image titled "sample." We are the Harbor Ridge Falcons.
Harbor Ridge Elementary
Address: 418 Marlow Fern, Irvine, CA 92781
Phone: (949) 555-0174
harborridge.oksd.example
Target Market(s)
Elementary School Families

```html
<!DOCTYPE html>
<html lang="en">
<head>
<meta charset="utf-8">
<title>Harbor Ridge Elementary School Letterhead</title>
<link href="https://fonts.googleapis.com/css2?family=Lato:wght@300;400;700&family=Open+Sans:wght@400&family=Pinyon+Script&display=swap" rel="stylesheet">
<style>
  :root {
    --backdrop: #e4e4e4;
    --paper: #f1f1f1;
    --navy: #24246a;
    --green: #3a9b43;
    --gray-text: #4a4a4a;
    --gray-soft: #6a6a6a;
    --ink: #1a1a1a;
    --mascot-faint: #e2e2e2;
  }
  * { box-sizing: border-box; margin: 0; padding: 0; }
  html, body {
    width: 1200px; height: 1200px; overflow: hidden;
    background: var(--backdrop);
  }
  .letterhead {
    position: absolute; left: 200px; top: 35px;
    width: 799px; height: 1130px;
    background: var(--paper);
    overflow: hidden;
    font-family: "Lato", sans-serif;
    color: var(--gray-text);
  }
  .brand {
    position: absolute; left: 56px; top: 62px;
    display: flex; align-items: center; gap: 14px;
  }
  .brand-mark {
    width: 72px; height: 72px; border-radius: 50%;
    background: var(--navy);
  }
  .brand-name {
    font-family: "Lato", sans-serif; font-weight: 700;
    font-size: 17px; line-height: 20px; color: var(--navy);
  }
  .contact {
    position: absolute; left: 520px; top: 67px;
    border-left: 2px solid var(--gray-soft);
    padding-left: 17px;
    font-family: "Open Sans", sans-serif; font-size: 13.5px;
    line-height: 16.5px; color: var(--gray-soft);
  }
  .contact li { list-style: none; display: flex; align-items: center; gap: 6px; }
  .contact svg { width: 10px; height: 10px; fill: var(--navy); flex: none; }
  .mascot-watermark {
    position: absolute; left: 450px; top: 735px;
    width: 360px; height: 340px;
    background: radial-gradient(ellipse at 55% 45%, var(--mascot-faint) 0%, rgba(226,226,226,0.6) 45%, rgba(241,241,241,0) 72%);
  }
  .letter {
    position: absolute; left: 85px; top: 247px; width: 629px;
    font-size: 13px; line-height: 18.8px; font-weight: 300;
  }
  .letter p { margin-bottom: 18.8px; text-align: justify; }
  .letter .date { margin-bottom: 19px; }
  .recipient { margin-bottom: 52px !important; }
  .recipient strong { font-weight: 700; color: var(--ink); }
  .salutation { margin-bottom: 18px; }
  .closing { margin-top: 56px; margin-bottom: 0 !important; }
  .signature {
    font-family: "Pinyon Script", cursive; font-size: 27px; line-height: 30px;
    color: var(--ink); margin-left: 6px; margin-top: 12px;
  }
  .footer-waves { position: absolute; left: 0; bottom: 0; width: 799px; height: 130px; }
</style>
</head>
<body>
  <main class="letterhead">
    <header>
      <div class="brand">
        <span class="brand-mark"></span>
        <div class="brand-name">Harbor Ridge<br>Falcons</div>
      </div>
      <ul class="contact">
        <li><svg viewBox="0 0 10 10"><path d="M2 0.5 L3.6 2.6 L2.7 3.6 C3.3 5 4.8 6.6 6.3 7.2 L7.3 6.3 L9.5 7.9 L8.5 9.5 C4.5 9.2 0.8 5.4 0.5 1.5Z"/></svg>(949) 555-0174</li>
        <li><svg viewBox="0 0 10 10"><circle cx="5" cy="5" r="4.5"/><path d="M0.5 5H9.5M5 0.5V9.5" stroke="#f1f1f1" stroke-width="0.8"/></svg>harborridge.oksd.example</li>
        <li><svg viewBox="0 0 10 10"><path d="M5 0C2.8 0 1.3 1.6 1.3 3.6 1.3 6.2 5 10 5 10S8.7 6.2 8.7 3.6C8.7 1.6 7.2 0 5 0Z M5 2.2A1.4 1.4 0 1 1 5 5 1.4 1.4 0 1 1 5 2.2Z"/></svg>418 Marlow Fern, Irvine, CA 92781</li>
      </ul>
    </header>

    <div class="mascot-watermark" role="img" aria-label="Faint large watermark of Flicker the Falcon mascot"></div>

    <section class="letter">
      <p class="date">01 January 2050</p>
      <p class="recipient"><strong>Company (Pvt) Ltd.</strong><br>PO Box 3355 Mainville St<br>Sample City Country 3355</p>
      <p class="salutation">Dear Nora Whitfield,</p>
      <p>Lorem ipsum dolor sit amet, consectetuer adipiscing elit, sed diam nonummy nibh euismod tincidunt ut laoreet dolore magna aliquam erat volutpat. Ut wisi enim ad minim veniam, quis nostrud exerci tation ullamcorper suscipit lobortis nisl ut aliquip ex ea commodo consequat. Duis dolore te feugait nulla facilisi. Nam liber tempor cum soluta nobis eleifend option congue nihil imperdiet doming id quod mazim placerat facer possim assum. Lorem ipsum dolor sit amet, consectetuer adipiscing elit, sed diam nonummy nibh euismod tincidunt ut laoreet dolore magna aliquam erat volutpat. Ut wisi enim ad minim veniam, quis nostrud exerci tation ullamcorper suscipit lobortis nisl ut aliquip ex ea commodo consequat.</p>
      <p>Consectetuer adipiscing elit, sed diam nonummy nibh euismod tincidunt ut laoreet dolore magna aliquam erat volutpat. Ut wisi enim ad minim veniam, quis nostrud exerci tation ullamcorper suscipit lobortis nisl ut aliquip ex ea commodo consequat. Consectetuer adipiscing elit, sed diam nonummy nibh euismod tincidunt ut laoreet dolore magna aliquam erat volutpat. Ut wisi enim ad minim veniam, quis nostrud exerci tation ullamcorper suscipit lobortis nisl ut aliquip ex ea commodo consequat.</p>
      <p>Consectetuer adipiscing elit, sed diam nonummy nibh euismod tincidunt ut laoreet dolore magna aliquam erat volutpat. Ut wisi enim ad minim veniam, quis nostrud exerci tation ullamcorper suscipit lobortis nisl ut aliquip ex ea commodo consequat. Consectetuer adipiscing elit, sed diam nonummy nibh euismod tincidunt ut laoreet dolore magna aliquam erat volutpat. Ut wisi enim ad minim veniam, quis nostrud exerci tation ullamcorper suscipit lobortis nisl ut aliquip ex ea commodo consequat.</p>
      <p class="closing">Sincerely Yours</p>
      <div class="signature">Daniel Reyes Marlowe</div>
    </section>

    <svg class="footer-waves" viewBox="0 0 799 130" preserveAspectRatio="none" aria-hidden="true">
      <path d="M0,20 C150,8 260,50 400,90 C560,112 700,78 799,26 V130 H0Z" fill="var(--green)"/>
      <path d="M0,40 C150,32 270,60 400,98 C560,118 700,92 799,42 V130 H0Z" fill="var(--paper)"/>
      <path d="M0,50 C150,40 280,70 400,103 C560,124 700,102 799,54 V130 H0Z" fill="var(--navy)"/>
      <path d="M0,78 C80,52 200,56 330,88 C470,118 640,122 799,100" fill="none" stroke="#ffffff" stroke-opacity="0.14" stroke-width="6"/>
    </svg>
  </main>
</body>
</html>
```